Refresh old packing for HGH product

At now product has design like on photo.
Target is to make new one based on this. New one should be more medical, and luxury looks.

Colors
0054AA
0677BA
7BADD7
CADEEF
E8F1F8

```html
<!DOCTYPE html>
<html lang="en">
<head>
<meta charset="utf-8">
<title>Somatropin carton dieline</title>
<link href="https://fonts.googleapis.com/css2?family=Montserrat:wght@400;500;600;700&display=swap" rel="stylesheet">
<style>
  :root {
    --blue-deep: #0054AA;
    --blue-brand: #0677BA;
    --blue-mid: #7BADD7;
    --blue-soft: #CADEEF;
    --blue-mist: #E8F1F8;
    --white: #ffffff;
    --cut-line: #6b6b6b;
    --page: #ffffff;
  }
  html, body {
    margin: 0;
    padding: 0;
    width: 1200px;
    height: 900px;
    overflow: hidden;
    background: var(--page);
    font-family: "Montserrat", sans-serif;
  }
  .canvas {
    position: relative;
    width: 1200px;
    height: 900px;
  }
  .dieline {
    position: absolute;
    left: 252px;
    top: 20px;
    width: 695px;
    height: 860px;
  }
  .cut { fill: none; stroke: var(--cut-line); stroke-width: 1.5; stroke-linejoin: round; }
  .fold { stroke: var(--cut-line); stroke-width: 1.2; }
  .fill-soft { fill: var(--blue-soft); }
  .fill-mid { fill: var(--blue-mid); }
  .fill-white { fill: var(--white); }
  .decor-area { fill: url(#decorTone); }
  .product-name { font-size: 24px; font-weight: 600; letter-spacing: 3px; fill: var(--blue-brand); }
  .product-sub { font-size: 8.2px; font-weight: 500; fill: var(--blue-brand); }
  .storage-info { font-size: 8.4px; font-weight: 500; fill: var(--blue-deep); text-anchor: end; }
  .lab-mark { font-size: 13px; font-weight: 600; letter-spacing: 2px; fill: var(--white); text-anchor: middle; }
  .back-heading { font-size: 10px; font-weight: 700; fill: var(--blue-deep); letter-spacing: 0.6px; }
  .back-text { font-size: 8.4px; font-weight: 400; fill: var(--blue-deep); }
  .back-lab { font-size: 7.6px; font-weight: 600; fill: var(--blue-deep); }
</style>
</head>
<body>
<main class="canvas">
  <svg class="dieline" viewBox="230 210 630 780" xmlns="http://www.w3.org/2000/svg" aria-label="Somatropin carton dieline">
    <defs>
      <clipPath id="bodyOutline">
        <path d="M280,621 L812,621 L812,625 L835,625 Q850,625 850,640 L850,895 Q850,910 835,910 L255,910 Q240,910 240,895 L240,640 Q240,625 255,625 L280,625 Z"/>
      </clipPath>
      <linearGradient id="decorTone" x1="0" y1="0" x2="1" y2="1">
        <stop offset="0" stop-color="#E8F1F8"/>
        <stop offset="1" stop-color="#CADEEF"/>
      </linearGradient>
    </defs>

    <!-- top tuck flap -->
    <polygon class="fill-soft" points="365,218 725,218 740,262 352,262"/>
    <!-- back panel -->
    <rect class="fill-soft" x="352" y="262" width="388" height="84"/>
    <rect class="fill-white" x="352" y="346" width="388" height="205"/>
    <!-- top side panel -->
    <rect class="fill-mid" x="352" y="551" width="388" height="70"/>
    <!-- front panel and sides, clipped to the rounded outline -->
    <g clip-path="url(#bodyOutline)">
      <rect class="fill-white" x="240" y="621" width="610" height="202"/>
      <rect class="fill-mid" x="240" y="823" width="218" height="87"/>
      <rect class="fill-soft" x="458" y="823" width="392" height="87"/>
    </g>
    <!-- bottom flap -->
    <polygon class="fill-mid" points="285,920 350,920 350,910 458,910 458,980 338,980 285,955"/>
    <polygon class="fill-soft" points="458,910 740,910 740,920 806,920 806,955 755,980 458,980"/>

    <!-- cut outlines -->
    <polygon class="cut" points="365,218 725,218 740,262 352,262"/>
    <rect class="cut" x="352" y="262" width="388" height="359"/>
    <line class="fold" x1="352" y1="551" x2="740" y2="551"/>
    <polygon class="cut" points="285,575 335,553 352,553 352,613 285,613"/>
    <polygon class="cut" points="740,553 757,553 806,575 806,613 740,613"/>
    <path class="cut" d="M280,621 L812,621 L812,625 L835,625 Q850,625 850,640 L850,895 Q850,910 835,910 L255,910 Q240,910 240,895 L240,640 Q240,625 255,625 L280,625 Z"/>
    <line class="fold" x1="280" y1="625" x2="280" y2="910"/>
    <line class="fold" x1="350" y1="621" x2="350" y2="910"/>
    <line class="fold" x1="740" y1="621" x2="740" y2="910"/>
    <line class="fold" x1="812" y1="625" x2="812" y2="910"/>
    <polygon class="cut" points="285,920 350,920 350,910 740,910 740,920 806,920 806,955 755,980 338,980 285,955"/>

    <!-- back panel copy (printed upside down) -->
    <g class="back-copy" transform="rotate(180 546 400)">
      <text class="back-heading" x="387" y="297">One vial contains :</text>
      <text class="back-text" x="387" y="313">3.33 mg somatropin (10IU), mannitol (E421), disodium phosphate</text>
      <text class="back-heading" x="387" y="341">KIT contains :</text>
      <text class="back-text" x="387" y="361">10*vial of human growth hormone</text>
      <text class="back-text" x="387" y="375">1*10 ml water for injection</text>
      <text class="back-heading" x="387" y="397">Caution :</text>
      <text class="back-text" x="387" y="414">Keep out of reach of children.</text>
      <text class="back-text" x="387" y="428">Store in refrigerator. Do not freeze.</text>
      <text class="back-text" x="387" y="442">Read the package leaflet before use.</text>
      <text class="back-text" x="387" y="470">For a weeks can be store in</text>
      <text class="back-text" x="387" y="484">room temperature</text>
      <text class="back-text" x="387" y="512">contact@orvelpharma.net</text>
      <circle cx="626" cy="505" r="10" fill="none" stroke="var(--blue-deep)" stroke-width="1.2"/>
      <text class="back-lab" x="642" y="504">ORVEL</text>
      <text class="back-lab" x="642" y="514">LABORATORIES</text>
    </g>

    <!-- front panel -->
    <rect class="decor-area" x="565" y="635" width="157" height="158" rx="6" role="img" aria-label="Decorative pattern of overlapping outlined hexagons in pale blue"/>
    <text class="product-name" x="397" y="696">SOMATROPIN</text>
    <text class="product-sub" x="397" y="709">SOMATROPIN(rDNA ORIGIN) FOR INJECTION</text>

    <text class="lab-mark" x="405" y="871">ORVEL</text>

    <text class="storage-info" x="726" y="872">Store between 2-8 C</text>
    <text class="storage-info" x="726" y="884">Protect from light. Do not shake</text>
    <text class="storage-info" x="729" y="897">100IU BOX - 10 VIAL x 10IU (3.33 MG)</text>
  </svg>
</main>
</body>
</html>
```